The Maple Arch Dental Offices Double-Sided A5 Flyer Highlighting Strengths & All Locations.

Designs are looking good. I just feel that they're too much in terms of content. Slight change in strategy. I would like a double sided A5 Flyer that has the following:

Front Side:

1. Brand (The Maple Arch Dental Offices). Use the logo that has Dental Offices beneath the words "The Maple Arch."
2. Highlight only the following keywords: Affordable. Friendly. Experienced Dental Care. Kids Friendly. We Accept All Insurance. 0% Interest Payment Plans.
3. Dental Services: Family Dentistry, Teeth Whitening, Braces, Implants, Veneers, Sedation.

Back Side:

This is where I want to highlight how convenient The Maple Arch is. We have 15 locations and growing. So here you can use our tagline:

We're Always Close By! With 15 Locations and Counting.

I want to list all 15 locations with each locations address and unique number. You can find those at https://maplearchsmiles.com/locations
The designer that can provide all locations in a catchy, easy to read and clean design will be selected.

The base of the flyer should utilize a white background. Keep it clean. Keep it fresh.

I'm looking to stand out from all competition with something unique and different. Get creative.

Target Market(s)

Women 30-40 years of age.

Industry/Entity Type

Dental

Font styles to use
Sans Serif

Colors
86cfc6
33b8a4
00a990
f59195
fdfdfb
fdf9cf
dddddd

Requirements
Must have
• Proper brand and color elements. Use white background.
Nice to have
• Surprise me with great ideas and design.
Should not have
• Prices.

```html
<!DOCTYPE html>
<html lang="en">
<head>
<meta charset="utf-8">
<title>The Maple Arch Dental Offices – A5 Flyer</title>
<link rel="stylesheet" href="https://fonts.googleapis.com/css2?family=Mulish:ital,wght@0,400;0,500;0,600;0,700;0,800;1,500;1,600&display=swap">
<style>
  :root {
    --backdrop: #4a4a4b;
    --paper: #ffffff;
    --ink: #222324;
    --ink-soft: #3c3d3f;
    --brand-grey: #6d6e71;
    --teal-blue: #3c9fb3;
    --teal: #33b8a4;
    --mint: #9fd8c0;
    --mint-soft: #c6e9d9;
    --rule: #cfe7dc;
    --blush: #f59195;
  }
  * { box-sizing: border-box; margin: 0; padding: 0; }
  html, body { width: 1200px; height: 873px; overflow: hidden; }
  body {
    background: var(--backdrop);
    font-family: "Mulish", Arial, sans-serif;
    color: var(--ink);
    position: relative;
  }
  .page {
    position: absolute;
    top: 45px;
    width: 550px;
    height: 781px;
    background: var(--paper);
    overflow: hidden;
  }
  .page--front { left: 40px; }
  .page--back { left: 609px; }

  /* Brand name */
  .brand { display: flex; align-items: center; gap: 10px; }
  .brand__dot {
    width: 36px; height: 36px; border-radius: 50%;
    background: var(--mint); flex: none;
  }
  .brand__text { color: var(--brand-grey); font-weight: 500; line-height: 1; white-space: nowrap; }
  .brand__name { display: block; font-size: 34px; letter-spacing: 0.2px; }
  .brand__sub { display: block; font-size: 9px; letter-spacing: 1.6px; text-transform: uppercase; margin-top: 6px; text-align: center; }

  .page--front .brand { position: absolute; top: 38px; left: 0; right: 0; justify-content: center; }

  /* Front: smile photo area */
  .smile-photo {
    position: absolute; left: 24px; top: 120px; width: 500px; height: 230px;
    border-radius: 48% 48% 50% 50% / 30% 30% 70% 70%;
    background: radial-gradient(ellipse at 50% 45%, #fbe9e4 0%, #efc7bb 45%, #dfa79a 80%, #f3ddd6 100%);
  }
  .swoosh { position: absolute; left: 0; top: 330px; width: 550px; height: 120px; }

  .headline {
    position: absolute; top: 469px; left: 0; right: 0; text-align: center;
    font-size: 30px; font-weight: 700; letter-spacing: 1.2px; color: var(--teal-blue);
  }

  .strengths { position: absolute; left: 65px; top: 503px; list-style: none; }
  .strengths li {
    width: 142px; font-size: 21px; font-style: italic; font-weight: 500;
    line-height: 28px; padding-top: 2px; border-bottom: 1.5px solid var(--mint);
    color: var(--ink);
  }
  .strengths li:last-child { border-bottom: none; }

  .services {
    position: absolute; left: 284px; top: 508px; width: 204px; height: 142px;
    border: 1px solid #9a9b9d; border-radius: 8px; overflow: hidden;
  }
  .services__title {
    background: var(--mint); font-size: 19px; font-weight: 600;
    padding: 2px 10px 1px; color: var(--ink);
  }
  .services__list { list-style: none; padding: 2px 14px 0 12px; }
  .services__list li {
    display: flex; align-items: center; gap: 9px;
    font-size: 16.5px; font-weight: 500; letter-spacing: 0.3px;
    height: 27px; border-bottom: 1.5px solid var(--mint-soft);
  }
  .services__list li:last-child { border-bottom: none; }
  .pin { width: 12px; height: 14px; flex: none; }

  .insurance {
    position: absolute; left: 65px; top: 680px;
    font-size: 14.5px; font-weight: 500; line-height: 18px;
  }
  .zero-rate { position: absolute; left: 170px; top: 667px; width: 110px; text-align: center; }
  .zero-rate__badge {
    width: 56px; height: 56px; margin: 0 auto; border-radius: 50%;
    background: var(--mint); color: #fff; font-weight: 800;
    display: flex; align-items: center; justify-content: center;
    font-size: 30px; padding-top: 4px; margin-top: -16px;
  }
  .zero-rate__badge small { font-size: 13px; margin-top: 8px; }
  .zero-rate__label { font-size: 10px; line-height: 11px; margin-top: -10px; color: var(--ink-soft); }

  .call { position: absolute; left: 284px; top: 697px; width: 204px; text-align: center; font-size: 17px; font-weight: 600; }
  .web-button {
    position: absolute; left: 284px; top: 723px; width: 204px; height: 24px;
    background: var(--teal-blue); color: #fff; border-radius: 4px;
    font-size: 15.5px; font-weight: 600; text-align: center; line-height: 24px;
  }

  .footer-band {
    position: absolute; left: 0; bottom: 0; width: 100%; height: 37px;
    background: var(--mint); text-align: center;
    font-size: 16.5px; font-weight: 700; line-height: 37px; color: var(--ink);
  }

  /* Back */
  .back-url { position: absolute; left: 33px; top: 38px; font-size: 16.5px; font-weight: 600; color: var(--teal-blue); letter-spacing: 0.3px; }
  .hero-photo {
    position: absolute; left: 330px; top: 0; width: 220px; height: 128px;
    background: linear-gradient(110deg, #eef5f8 0%, #dbe8ee 40%, #f4d3cf 75%, #e9b3ad 100%);
  }
  .tagline {
    position: absolute; left: 25px; top: 67px; width: 305px; height: 61px;
    background: var(--mint); padding: 8px 11px;
  }
  .tagline__title { display: block; font-size: 18px; font-weight: 700; line-height: 22px; }
  .tagline__sub { display: block; font-size: 16.5px; font-weight: 500; line-height: 22px; }

  .locations {
    position: absolute; left: 25px; top: 152px; width: 510px;
    display: grid; grid-template-columns: 166px 177px 167px;
    grid-template-rows: repeat(5, 118px);
  }
  .location {
    padding-left: 4px; font-size: 10.6px; line-height: 14px;
    color: var(--ink-soft); overflow: hidden; white-space: nowrap;
  }
  .location__city { font-size: 11px; font-weight: 800; color: var(--teal-blue); letter-spacing: 0.2px; margin-bottom: 3px; line-height: 14px; }
  .location__office { margin-bottom: 4px; }
  .location__line { display: flex; gap: 4px; }
  .location__phone { display: flex; align-items: center; gap: 4px; margin-top: 4px; }
  .icon { width: 10px; height: 10px; flex: none; margin-top: 2px; }
  .location__phone .icon { margin-top: 0; }
  .location--rule { border-top: 1px solid var(--rule); padding-top: 6px; }
  .location--first { padding-top: 0; border-top: none; }

  .page--back .brand {
    position: absolute; left: 355px; top: 645px; width: 170px;
    flex-direction: column; gap: 6px;
  }
  .page--back .brand__dot { width: 30px; height: 30px; }
  .page--back .brand__name { font-size: 24px; }
  .page--back .brand__sub { font-size: 7px; margin-top: 5px; }
</style>
</head>
<body>

<!-- FRONT -->
<section class="page page--front">
  <div class="brand">
    <span class="brand__dot"></span>
    <span class="brand__text">
      <span class="brand__name">The Maple Arch</span>
      <span class="brand__sub">Dental Offices</span>
    </span>
  </div>

  <div class="smile-photo" role="img" aria-label="Collage of smiling faces arranged in the shape of a smile"></div>

  <svg class="swoosh" viewBox="0 0 550 120" aria-hidden="true">
    <path d="M0 50 C150 110 380 95 550 40 L550 120 L0 120 Z" fill="#fff"/>
    <path d="M0 52 C160 102 380 82 550 26 L550 44 C380 96 170 116 0 64 Z" fill="#9fd8c0"/>
    <path d="M0 60 C160 108 380 92 550 40 L550 50 C380 104 170 122 0 72 Z" fill="#3c9fb3"/>
  </svg>

  <h1 class="headline">WE CARE FOR YOUR SMILE</h1>

  <ul class="strengths">
    <li>Affordable</li>
    <li>Friendly</li>
    <li>Experienced</li>
    <li>Dental Care</li>
    <li>Kids Friendly</li>
  </ul>

  <div class="services">
    <div class="services__title">Dental Services</div>
    <ul class="services__list">
      <li><svg class="pin" viewBox="0 0 12 14"><path d="M6 0a5.5 5.5 0 0 0-5.5 5.5C.5 9.5 6 14 6 14s5.5-4.5 5.5-8.5A5.5 5.5 0 0 0 6 0z" fill="#9fd8c0"/><circle cx="6" cy="5.5" r="2" fill="#3c9fb3"/></svg>Family Dentistry</li>
      <li><svg class="pin" viewBox="0 0 12 14"><path d="M6 0a5.5 5.5 0 0 0-5.5 5.5C.5 9.5 6 14 6 14s5.5-4.5 5.5-8.5A5.5 5.5 0 0 0 6 0z" fill="#9fd8c0"/><circle cx="6" cy="5.5" r="2" fill="#3c9fb3"/></svg>Teeth Whitening</li>
      <li><svg class="pin" viewBox="0 0 12 14"><path d="M6 0a5.5 5.5 0 0 0-5.5 5.5C.5 9.5 6 14 6 14s5.5-4.5 5.5-8.5A5.5 5.5 0 0 0 6 0z" fill="#9fd8c0"/><circle cx="6" cy="5.5" r="2" fill="#3c9fb3"/></svg>Braces, Implants</li>
      <li><svg class="pin" viewBox="0 0 12 14"><path d="M6 0a5.5 5.5 0 0 0-5.5 5.5C.5 9.5 6 14 6 14s5.5-4.5 5.5-8.5A5.5 5.5 0 0 0 6 0z" fill="#9fd8c0"/><circle cx="6" cy="5.5" r="2" fill="#3c9fb3"/></svg>Veneers, Sedation</li>
    </ul>
  </div>

  <p class="insurance">We Accept<br>All Insurance</p>
  <div class="zero-rate">
    <div class="zero-rate__badge">0<small>%</small></div>
    <p class="zero-rate__label">Interest<br>Payment Plans.</p>
  </div>

  <p class="call">Call us 888-555-0147</p>
  <p class="web-button">www.maplearchsmiles.com</p>

  <p class="footer-band">We offer affordable care with locations open 7 days a week</p>
</section>

<!-- BACK -->
<section class="page page--back">
  <p class="back-url">www.maplearchsmiles.com</p>
  <div class="hero-photo" role="img" aria-label="Close-up of a smile during a dental check-up"></div>
  <div class="tagline">
    <span class="tagline__title">We're Always Close By!</span>
    <span class="tagline__sub">With 15 Locations and Counting.</span>
  </div>

  <svg width="0" height="0" style="position:absolute" aria-hidden="true">
    <defs>
      <symbol id="i-pin" viewBox="0 0 10 10"><circle cx="5" cy="5" r="5" fill="#33b8a4"/><circle cx="5" cy="4.3" r="1.8" fill="#fff"/></symbol>
      <symbol id="i-phone" viewBox="0 0 10 10"><circle cx="5" cy="5" r="5" fill="#33b8a4"/><path d="M3.3 2.6l1 1-.5.7c.4.8 1 1.4 1.8 1.8l.7-.5 1 1-.6.8C4.9 7.2 2.8 5.1 2.5 3.2z" fill="#fff"/></symbol>
    </defs>
  </svg>

  <div class="locations">
    <article class="location location--first">
      <h3 class="location__city">BARRIE</h3>
      <p class="location__office">Dental Office at Lakeview Mall</p>
      <p class="location__line"><svg class="icon"><use href="#i-pin"/></svg><span>410 Harbourline Street<br>Unit 12B (in Lakeview Mall)<br>Barrie ON, L4N 0A1</span></p>
      <p class="location__phone"><svg class="icon"><use href="#i-phone"/></svg>(705) 555-0142</p>
    </article>
    <article class="location location--first">
      <h3 class="location__city">BRAMPTON</h3>
      <p class="location__office">Dental Office at Greenfield Plaza</p>
      <p class="location__line"><svg class="icon"><use href="#i-pin"/></svg><span>88 Willowmere Parkway<br>Unit 204, Greenfield Plaza<br>Brampton ON, L6Y 0B2</span></p>
      <p class="location__phone"><svg class="icon"><use href="#i-phone"/></svg>647-555-0118</p>
    </article>
    <article class="location location--first">
      <h3 class="location__city">DUNDAS</h3>
      <p class="location__office">Dental Office on Mill St. E.</p>
      <p class="location__line"><svg class="icon"><use href="#i-pin"/></svg><span>27 Mill Street East<br>Unit 4<br>Dundas, ON L9H 0C3</span></p>
      <p class="location__phone"><svg class="icon"><use href="#i-phone"/></svg>(289) 555-0176</p>
    </article>

    <article class="location location--rule">
      <h3 class="location__city">BRANTFORD</h3>
      <p class="location__office">Dental Office on Orchard<br>Hill St.</p>
      <p class="location__line"><svg class="icon"><use href="#i-pin"/></svg><span>215 Orchard Hill St.<br>Brantford ON, N3R 0D4</span></p>
      <p class="location__phone"><svg class="icon"><use href="#i-phone"/></svg>(519) 555-0133</p>
    </article>
    <article class="location location--rule">
      <h3 class="location__city">BRANTFORD</h3>
      <p class="location__office">Dental Office on Riverside St. W.</p>
      <p class="location__line"><svg class="icon"><use href="#i-pin"/></svg><span>59 Riverside Street West<br>Unit 3C<br>Brantford ON, N3T 0E5</span></p>
      <p class="location__phone"><svg class="icon"><use href="#i-phone"/></svg>(519) 555-0191</p>
    </article>
    <article class="location location--rule">
      <h3 class="location__city">STONEY CREEK</h3>
      <p class="location__office">Dental Office In Stoney Creek/<br>Hamilton</p>
      <p class="location__line"><svg class="icon"><use href="#i-pin"/></svg><span>610 Ridgeway Rd, Unit #2<br>Stoney Creek ON, L8G 0F6</span></p>
      <p class="location__phone"><svg class="icon"><use href="#i-phone"/></svg>289-555-0164</p>
    </article>

    <article class="location location--rule">
      <h3 class="location__city">MISSISSAUGA</h3>
      <p class="location__office">Dental Office on Cedarglen Rd.</p>
      <p class="location__line"><svg class="icon"><use href="#i-pin"/></svg><span>2250 Cedarglen Road<br>Unit 105<br>Mississauga, ON L4Y 0G7</span></p>
      <p class="location__phone"><svg class="icon"><use href="#i-phone"/></svg>(647) 555-0127</p>
    </article>
    <article class="location location--rule">
      <h3 class="location__city">MISSISSAUGA</h3>
      <p class="location__office">Dental Office on Birch Rd. E.</p>
      <p class="location__line"><svg class="icon"><use href="#i-pin"/></svg><span>4120 Birch Road East<br>Unit 210<br>Mississauga ON, L4T 0H8</span></p>
      <p class="location__phone"><svg class="icon"><use href="#i-phone"/></svg>(647) 555-0159</p>
    </article>
    <article class="location location--rule">
      <h3 class="location__city">MISSISSAUGA</h3>
      <p class="location__office">Dental Office at Northgate Mall</p>
      <p class="location__line"><svg class="icon"><use href="#i-pin"/></svg><span>512 Northgate Blvd. E. #118<br>Northgate Mall (2nd Floor)<br>Mississauga ON, L5A 0J9</span></p>
      <p class="location__phone"><svg class="icon"><use href="#i-phone"/></svg>647-555-0185</p>
    </article>

    <article class="location location--rule">
      <h3 class="location__city">SCARBOROUGH</h3>
      <p class="location__office">Dental Office at Elmwood Plaza</p>
      <p class="location__line"><svg class="icon"><use href="#i-pin"/></svg><span>1875 Elmwood Ave. East<br>Unit 6<br>Scarborough ON, M1R 0K1</span></p>
      <p class="location__phone"><svg class="icon"><use href="#i-phone"/></svg>(647) 555-0102</p>
    </article>
    <article class="location location--rule">
      <h3 class="location__city">SCARBOROUGH</h3>
      <p class="location__office">Dental Office at Foxridge Square</p>
      <p class="location__line"><svg class="icon"><use href="#i-pin"/></svg><span>3390 Foxridge Road<br>Scarborough ON,<br>M1E 0L2</span></p>
      <p class="location__phone"><svg class="icon"><use href="#i-phone"/></svg>(647) 555-0148</p>
    </article>
    <article class="location location--rule">
      <h3 class="location__city">SCARBOROUGH</h3>
      <p class="location__office">Dental Office on Hollis Rd.</p>
      <p class="location__line"><svg class="icon"><use href="#i-pin"/></svg><span>1640 Hollis Road<br>Unit 9<br>Scarborough ON, M1P 0M3</span></p>
      <p class="location__phone"><svg class="icon"><use href="#i-phone"/></svg>(647) 555-0170</p>
    </article>

    <article class="location location--rule">
      <h3 class="location__city">ETOBICOKE</h3>
      <p class="location__office">Dental Office on<br>Pinecrest Grove Rd.</p>
      <p class="location__line"><svg class="icon"><use href="#i-pin"/></svg><span>1980 Pinecrest Grove Road<br>Unit 5<br>Etobicoke ON, M9V 0N4</span></p>
      <p class="location__phone"><svg class="icon"><use href="#i-phone"/></svg>(647) 555-0139</p>
    </article>
    <article class="location location--rule">
      <h3 class="location__city">ETOBICOKE</h3>
      <p class="location__office">Dental Office on Harbour<br>College Blvd</p>
      <p class="location__line"><svg class="icon"><use href="#i-pin"/></svg><span>75 Harbour College Blvd<br>Unit 108<br>Etobicoke, ON M9V 0P5</span></p>
      <p class="location__phone"><svg class="icon"><use href="#i-phone"/></svg>(647) 555-0194</p>
    </article>
  </div>

  <div class="brand">
    <span class="brand__dot"></span>
    <span class="brand__text">
      <span class="brand__name">The Maple Arch</span>
      <span class="brand__sub">Dental Offices</span>
    </span>
  </div>

  <p class="footer-band">We offer affordable care with locations open 7 days a week</p>
</section>

</body>
</html>
```